Management consulting Company in the electronic payment ecosystem needs a Website

We need to have a "showcase" style website that contains the key message that our company is able to provide management consulting in the world of payment systems. Our mission is to assist our clients in reviewing their sales, purchasing, operation and IT processes and to support them in identifying the best solution in the use of payment systems.

```html
<!DOCTYPE html>
<html lang="en">
<head>
<meta charset="utf-8">
<title>Paxora Consulting</title>
<link rel="stylesheet" href="https://fonts.googleapis.com/css2?family=Roboto:wght@300;400;500;700&display=swap">
<style>
:root{
  --navy:#0a1560;
  --navy-deep:#071047;
  --ink:#222;
  --muted:#666;
  --light:#f2f2f2;
  --grey-band:#e4e4e4;
  --footer:#1e1e1e;
  --footer-bar:#0a1560;
  --white:#fff;
}
*{box-sizing:border-box;margin:0;padding:0}
html,body{width:1200px;height:3768px;overflow:hidden}
body{font-family:"Roboto",Arial,sans-serif;color:var(--ink);background:var(--white);position:relative}

/* header */
.site-header{position:absolute;left:0;top:0;width:1200px;height:148px;background:var(--white)}
.brand{position:absolute;display:flex;align-items:center;gap:12px;font-weight:700;color:var(--navy)}
.brand .dot{border-radius:50%;background:var(--navy)}
.site-header .brand{left:80px;top:40px;font-size:40px}
.site-header .brand .dot{width:48px;height:48px}
.topbar{position:absolute;right:112px;top:50px;display:flex;gap:28px;font-size:14px;color:var(--ink)}
.topbar span{display:flex;align-items:center;gap:8px}
.main-nav{position:absolute;right:100px;top:92px;display:flex;gap:8px;font-size:15px;font-weight:500;color:var(--ink)}
.main-nav a{padding:8px 12px;text-decoration:none;color:inherit;border:2px solid transparent;border-radius:10px}
.main-nav a.active{border-color:var(--navy);color:var(--navy)}

/* hero */
.hero{position:absolute;left:0;top:148px;width:1200px;height:632px;
  background:radial-gradient(circle at 50% 45%,#2b3c5a 0%,#111a2b 55%,#05080f 100%)}
.hero .brand{left:0;right:0;top:190px;justify-content:center;color:var(--white);font-size:120px}
.hero .brand .dot{width:130px;height:130px;background:none;border:12px solid var(--white)}
.hero-tagline{position:absolute;left:0;right:0;top:396px;text-align:center;color:var(--white);font-size:28px;font-weight:300;letter-spacing:.5px}

/* feature cards */
.feature-card{position:absolute;top:720px;width:308px;height:368px;background:var(--white);box-shadow:0 4px 18px rgba(0,0,0,.25);text-align:center;padding-top:36px}
.feature-card .icon-ring{width:150px;height:150px;margin:0 auto;border-radius:50%;border:10px solid var(--navy);display:flex;align-items:center;justify-content:center}
.feature-card .icon-ring i{display:block;width:82px;height:82px;border-radius:50%;background:#c9cde0}
.feature-card h3{font-size:20px;font-weight:700;margin-top:26px;letter-spacing:.5px}
.feature-card p{font-size:14px;font-weight:500;line-height:1.35;margin:14px auto 0;width:230px}
.go{display:inline-block;margin-top:18px}
.feature-card.featured{background:var(--navy);color:var(--white)}
.feature-card.featured .icon-ring{border-color:var(--white)}
.feature-card.featured .icon-ring i{background:#3a4690}

/* about */
.about{position:absolute;left:0;top:1160px;width:1200px;height:540px;background:var(--grey-band)}
.about h2{position:absolute;left:112px;top:100px;font-size:48px;font-weight:700;color:var(--navy)}
.about h2 span{font-weight:400}
.about .rule{position:absolute;left:112px;top:162px;width:400px;height:3px;background:var(--navy)}
.about .lead{position:absolute;left:112px;top:180px;font-size:20px;font-weight:700;color:var(--navy)}
.about .body{position:absolute;left:112px;top:222px;width:430px;font-size:14px;line-height:1.55;color:var(--muted)}
.btn-dark{display:inline-block;background:var(--navy);color:var(--white);font-size:13px;font-weight:700;padding:12px 16px;border-radius:6px}
.about .btn-dark{position:absolute;left:112px;top:390px}
.about .photo{position:absolute;left:620px;top:104px;width:468px;height:324px;background:linear-gradient(135deg,#0e2a55,#2a7fb8 60%,#a7d4ef)}

/* services */
.service-card{position:absolute;width:308px;height:364px;background:var(--white);box-shadow:0 2px 10px rgba(0,0,0,.18);text-align:center}
.service-card .photo{height:180px}
.service-card h3{font-size:20px;font-weight:700;margin-top:26px;letter-spacing:.5px}
.service-card p{font-size:14px;color:var(--muted);line-height:1.4;width:220px;margin:10px auto 0}
.service-card .go{margin-top:14px}

/* contact band */
.contact-band{position:absolute;left:0;top:2608px;width:1200px;height:352px;background:var(--navy)}
.contact-band .brand{left:150px;top:108px;color:var(--white);font-size:44px}
.contact-band .brand .dot{width:130px;height:130px;background:none;border:12px solid var(--white)}
.contact-band h2{position:absolute;left:460px;width:560px;top:56px;text-align:center;color:var(--white);font-size:36px;font-weight:300}
.field{position:absolute;color:#cfd3ee;font-size:14px;border-bottom:1px solid #8e95c8;padding-bottom:8px}
.btn-outline{position:absolute;left:640px;top:248px;width:176px;height:60px;border:2px solid var(--white);border-radius:30px;color:var(--white);font-size:20px;font-weight:300;display:flex;align-items:center;justify-content:center}

/* blog */
.blog h2{position:absolute;left:0;right:0;top:3040px;text-align:center;font-size:52px;font-weight:700;color:var(--navy)}
.blog h2 span{font-weight:400}
.blog .rule{position:absolute;left:480px;top:3106px;width:240px;height:3px;background:var(--navy)}
.blog .lead{position:absolute;left:0;right:0;top:3118px;text-align:center;font-size:20px;font-weight:700;color:var(--navy)}
.post{position:absolute;top:3188px;width:470px;height:220px}
.post .date{position:absolute;left:0;top:0;width:46px;height:48px;background:var(--navy);color:var(--white);font-size:26px;font-weight:700;display:flex;align-items:center;justify-content:center}
.post h3{position:absolute;left:56px;top:2px;width:168px;font-size:17px;font-weight:700;color:var(--navy);line-height:1.3;white-space:nowrap}
.post h3 .sub{display:block;margin-top:4px;font-size:12px;font-weight:400;color:var(--muted)}
.post p{position:absolute;left:0;top:66px;width:220px;font-size:13px;color:var(--muted);line-height:1.45}
.post .btn-dark{position:absolute;left:0;top:160px;font-size:11px;padding:8px 12px}
.post .photo{position:absolute;left:236px;top:0;width:230px;height:190px}

/* footer */
.site-footer{position:absolute;left:0;top:3436px;width:1200px;height:304px;background:var(--footer);color:var(--white)}
.site-footer .brand{left:112px;top:110px;color:var(--white);font-size:52px}
.site-footer .brand .dot{width:60px;height:60px;background:var(--white)}
.site-footer h4{position:absolute;top:48px;font-size:24px;font-weight:400}
.contact-list{position:absolute;left:400px;top:100px;font-size:14px;line-height:1.4;list-style:none}
.contact-list li{display:flex;gap:12px;margin-bottom:16px;width:240px}
.quick-links{position:absolute;left:700px;top:100px;list-style:none;font-size:14px;line-height:1.85}
.social{position:absolute;left:888px;top:100px;display:grid;grid-template-columns:repeat(3,48px);gap:16px 18px}
.social span{width:48px;height:48px;border-radius:50%;border:2px solid var(--white);display:flex;align-items:center;justify-content:center}
.copyright{position:absolute;left:0;top:3740px;width:1200px;height:28px;background:var(--footer-bar);color:var(--white);font-size:13px;text-align:center;line-height:28px}
</style>
</head>
<body>

<header class="site-header">
  <div class="brand"><span class="dot"></span>Paxora</div>
  <div class="topbar">
    <span><svg width="14" height="14" viewBox="0 0 24 24"><path fill="#222" d="M6.6 10.8a15 15 0 0 0 6.6 6.6l2.2-2.2a1 1 0 0 1 1-.25 11.4 11.4 0 0 0 3.6.57 1 1 0 0 1 1 1V20a1 1 0 0 1-1 1A17 17 0 0 1 3 4a1 1 0 0 1 1-1h3.5a1 1 0 0 1 1 1c0 1.25.2 2.450 .57 3.57a1 1 0 0 1-.25 1z"/></svg>555-014-2290</span>
    <span><svg width="16" height="12" viewBox="0 0 16 12"><rect x="0.5" y="0.5" width="15" height="11" fill="#222"/><path d="M1 1l7 5 7-5" stroke="#fff" fill="none"/></svg>hello@paxora-consult.com</span>
    <span><svg width="14" height="14" viewBox="0 0 14 14"><circle cx="7" cy="4" r="3" fill="#222"/><path d="M1 14a6 6 0 0 1 12 0z" fill="#222"/></svg>Sign in</span>
  </div>
  <nav class="main-nav">
    <a class="active">HOME</a><a>ABOUT US</a><a>SERVICES</a><a>FEATURES</a><a>BLOG</a><a>CONTACT</a>
  </nav>
</header>

<section class="hero" role="img" aria-label="Dark photo of a consultant touching a glowing network of payment icons">
  <div class="brand"><span class="dot"></span>Paxora</div>
  <p class="hero-tagline">MANAGEMENT CONSULTING COMPANY PROVIDING CONSULTATION</p>
</section>

<article class="feature-card" style="left:112px">
  <div class="icon-ring"><i role="img" aria-label="Payment icon"></i></div>
  <h3>PAYMENT CONSULTING</h3>
  <p>There are many variations of passages of Lorem Ipsum available, but the majority have suffered alteration in some.</p>
  <svg class="go" width="28" height="28" viewBox="0 0 28 28"><circle cx="14" cy="14" r="14" fill="#0a1560"/><path d="M8 14h11M15 9l5 5-5 5" stroke="#fff" stroke-width="2.5" fill="none"/></svg>
</article>
<article class="feature-card featured" style="left:446px">
  <div class="icon-ring"><i role="img" aria-label="Sales team icon"></i></div>
  <h3>SALES CONSULTING</h3>
  <p>There are many variations of passages of Lorem Ipsum available, but the majority have suffered alteration in some.</p>
  <svg class="go" width="28" height="28" viewBox="0 0 28 28"><circle cx="14" cy="14" r="14" fill="#fff"/><path d="M8 14h11M15 9l5 5-5 5" stroke="#0a1560" stroke-width="2.5" fill="none"/></svg>
</article>
<article class="feature-card" style="left:780px">
  <div class="icon-ring"><i role="img" aria-label="Purchasing gear icon"></i></div>
  <h3>PURCHASING CONSULTING</h3>
  <p>There are many variations of passages of Lorem Ipsum available, but the majority have suffered alteration in some.</p>
  <svg class="go" width="28" height="28" viewBox="0 0 28 28"><circle cx="14" cy="14" r="14" fill="#0a1560"/><path d="M8 14h11M15 9l5 5-5 5" stroke="#fff" stroke-width="2.5" fill="none"/></svg>
</article>

<section class="about">
  <h2>ABOUT <span>US</span></h2>
  <div class="rule"></div>
  <p class="lead">We Providing consultation in the payment ecosystem</p>
  <p class="body">We help businesses review how they sell, buy, operate and run their IT so that every payment flow fits the way they work. Our team studies current processes, compares the options on the market and guides each client to the payment solution that suits them best, from first review to launch and beyond, with clear advice at every step.</p>
  <span class="btn-dark">READ MORE</span>
  <div class="photo" role="img" aria-label="Hand touching a digital screen labelled consulting"></div>
</section>

<article class="service-card" style="left:112px;top:1748px">
  <div class="photo" role="img" aria-label="Business meeting photo" style="background:linear-gradient(135deg,#8a7f74,#d9d2c8)"></div>
  <h3>MANAGEMENT</h3><p>Low Voltage Wiring and Cabling Voice and Data Network Cabling</p>
  <svg class="go" width="26" height="26" viewBox="0 0 28 28"><circle cx="14" cy="14" r="14" fill="#0a1560"/><path d="M8 14h11M15 9l5 5-5 5" stroke="#fff" stroke-width="2.5" fill="none"/></svg>
</article>
<article class="service-card" style="left:446px;top:1748px">
  <div class="photo" role="img" aria-label="Consultants reviewing charts photo" style="background:linear-gradient(135deg,#5d6670,#c7ccd2)"></div>
  <h3>CONSULTING</h3><p>Low Voltage Wiring and Cabling Voice and Data Network Cabling</p>
  <svg class="go" width="26" height="26" viewBox="0 0 28 28"><circle cx="14" cy="14" r="14" fill="#0a1560"/><path d="M8 14h11M15 9l5 5-5 5" stroke="#fff" stroke-width="2.5" fill="none"/></svg>
</article>
<article class="service-card" style="left:780px;top:1748px">
  <div class="photo" role="img" aria-label="City skyline at sunset photo" style="background:linear-gradient(160deg,#f3e6c4,#8c8a84)"></div>
  <h3>PAYMENT</h3><p>Low Voltage Wiring and Cabling Voice and Data Network Cabling</p>
  <svg class="go" width="26" height="26" viewBox="0 0 28 28"><circle cx="14" cy="14" r="14" fill="#0a1560"/><path d="M8 14h11M15 9l5 5-5 5" stroke="#fff" stroke-width="2.5" fill="none"/></svg>
</article>
<article class="service-card" style="left:112px;top:2184px">
  <div class="photo" role="img" aria-label="Team at a table photo" style="background:linear-gradient(135deg,#6b6358,#cfc7ba)"></div>
  <h3>ECOSYSTEM</h3><p>Low Voltage Wiring and Cabling Voice and Data Network Cabling</p>
  <svg class="go" width="26" height="26" viewBox="0 0 28 28"><circle cx="14" cy="14" r="14" fill="#0a1560"/><path d="M8 14h11M15 9l5 5-5 5" stroke="#fff" stroke-width="2.5" fill="none"/></svg>
</article>
<article class="service-card" style="left:446px;top:2184px">
  <div class="photo" role="img" aria-label="Colleagues discussing documents photo" style="background:linear-gradient(135deg,#7a6f66,#e0d8cf)"></div>
  <h3>PURCHASING</h3><p>Low Voltage Wiring and Cabling Voice and Data Network Cabling</p>
  <svg class="go" width="26" height="26" viewBox="0 0 28 28"><circle cx="14" cy="14" r="14" fill="#0a1560"/><path d="M8 14h11M15 9l5 5-5 5" stroke="#fff" stroke-width="2.5" fill="none"/></svg>
</article>
<article class="service-card" style="left:780px;top:2184px">
  <div class="photo" role="img" aria-label="Office workshop photo" style="background:linear-gradient(135deg,#5f5a55,#bdb5ab)"></div>
  <h3>IT PROCESSES</h3><p>Low Voltage Wiring and Cabling Voice and Data Network Cabling</p>
  <svg class="go" width="26" height="26" viewBox="0 0 28 28"><circle cx="14" cy="14" r="14" fill="#0a1560"/><path d="M8 14h11M15 9l5 5-5 5" stroke="#fff" stroke-width="2.5" fill="none"/></svg>
</article>

<section class="contact-band">
  <div class="brand"><span class="dot"></span>Paxora</div>
  <h2>Get in touch with us</h2>
  <span class="field" style="left:464px;top:130px;width:250px">* Your Name</span>
  <span class="field" style="left:750px;top:130px;width:260px">* Your e-mail</span>
  <span class="field" style="left:464px;top:190px;width:546px">* Your Message</span>
  <span class="btn-outline">Get in touch</span>
</section>

<section class="blog">
  <h2>LATEST <span>BLOG</span></h2>
  <div class="rule"></div>
  <p class="lead">We Providing consultation in the payment ecosystem</p>
  <article class="post" style="left:112px">
    <span class="date">05</span>
    <h3>Dummy text of the<span class="sub">Lorem Ipsum has been</span></h3>
    <p>There are many variations of the list of passages of Lorem Ipsum available, but the majority have suffered alteration in some.</p>
    <span class="btn-dark">READ MORE</span>
    <div class="photo" role="img" aria-label="Businessman working at a laptop photo" style="background:linear-gradient(135deg,#b9c4cf,#eef1f4)"></div>
  </article>
  <article class="post" style="left:612px">
    <span class="date">07</span>
    <h3>Dummy text of the<span class="sub">Lorem Ipsum has been</span></h3>
    <p>There are many variations of the list of passages of Lorem Ipsum available, but the majority have suffered alteration in some.</p>
    <span class="btn-dark">READ MORE</span>
    <div class="photo" role="img" aria-label="Smiling consultant at a desk photo" style="background:linear-gradient(135deg,#6d5a4c,#d8cbbf)"></div>
  </article>
</section>

<footer class="site-footer">
  <div class="brand"><span class="dot"></span>Paxora</div>
  <h4 style="left:400px">Contact Us</h4>
  <ul class="contact-list">
    <li><svg width="14" height="18" viewBox="0 0 14 18"><path d="M7 0a7 7 0 0 1 7 7c0 5-7 11-7 11S0 12 0 7a7 7 0 0 1 7-7z" fill="#fff"/><circle cx="7" cy="7" r="2.5" fill="#1e1e1e"/></svg>No 12 B, Harbor Lane Street, 40 and Sample 2222</li>
    <li><svg width="14" height="14" viewBox="0 0 24 24"><path fill="#fff" d="M6.6 10.8a15 15 0 0 0 6.6 6.6l2.2-2.2a1 1 0 0 1 1-.25 11.4 11.4 0 0 0 3.6.57 1 1 0 0 1 1 1V20a1 1 0 0 1-1 1A17 17 0 0 1 3 4a1 1 0 0 1 1-1h3.5a1 1 0 0 1 1 1c0 1.25.2 2.45.57 3.57a1 1 0 0 1-.25 1z"/></svg>555-014-2290</li>
    <li><svg width="16" height="12" viewBox="0 0 16 12"><rect x=".5" y=".5" width="15" height="11" fill="#fff"/><path d="M1 1l7 5 7-5" stroke="#1e1e1e" fill="none"/></svg>hello@paxora-consult.com</li>
  </ul>
  <h4 style="left:700px">Quick Link</h4>
  <ul class="quick-links"><li>Home</li><li>About Us</li><li>Services</li><li>Features</li><li>Blog</li></ul>
  <h4 style="left:888px">Marketing Link</h4>
  <div class="social">
    <span></span>
    <span><svg width="20" height="14" viewBox="0 0 16 12"><rect x=".5" y=".5" width="15" height="11" fill="#fff"/><path d="M1 1l7 5 7-5" stroke="#1e1e1e" fill="none"/></svg></span>
    <span><svg width="20" height="20" viewBox="0 0 20 20"><circle cx="8" cy="8" r="6" stroke="#fff" stroke-width="2.5" fill="none"/><path d="M12.5 12.5l6 6" stroke="#fff" stroke-width="2.5"/></svg></span>
    <span><svg width="14" height="20" viewBox="0 0 14 18"><path d="M7 0a7 7 0 0 1 7 7c0 5-7 11-7 11S0 12 0 7a7 7 0 0 1 7-7z" fill="#fff"/><circle cx="7" cy="7" r="2.5" fill="#1e1e1e"/></svg></span>
    <span></span>
    <span></span>
  </div>
</footer>
<div class="copyright">Copyright © 2021 Paxora Consulting. All Rights Reserved.</div>

</body>
</html>
```